Recreating a Opt-in for a FREE BOOK for brides.

I need to have an opt-in box recreated to make brides want to get my free book. The opt-in message is already on the mock website. It needs to look graphically pleasing in the colors being used, but bold enough to grab the viewers attention. I am including the link to the website where the graphic needs to be re-created. You'll notice there are two areas where the graphics need to go.

Target Market(s)

Brides

Requirements
Must have
• Begin by looking at the website..http://plorvex.com/tu-gami/
On the homepage is the current "A Gift For You" graphic. (I have included an image of the home page for the circled area that needs to be recreated.) As of now, the graphics looks amateurish. It needs your professional upgrade. The image of the book has also been uploaded as a file for you to use.

In addition, on the FAQ page, there is a graphic that has been created to fit that area of the page to get the book (circled area of the graphic has been uploaded). I need to have the same graphic you are creating for the home page, but adjust it to be placed on this page. When you recreate the graphic for the FAQ page, there are 2 changes to the text:

1. Change the word "Receive" to "Download." (The rest of the sentence should stay the same.)
2. Delete the entire sentence "Or, pay $17.95 at zentrabo or corliss and pembe by clicking here.
Nice to have
• Normal file formats such as jpeg, photoshop or ai are fine.

```html
<!DOCTYPE html>
<html lang="en">
<head>
<meta charset="utf-8">
<title>The Sugar Atelier – Wedding Cakes</title>
<link rel="stylesheet" href="https://fonts.googleapis.com/css2?family=Great+Vibes&family=Caveat:wght@700&family=Lato:wght@400;700;900&family=Montserrat:wght@500;600;700;800&display=swap">
<style>
  :root {
    --page-bg: #f4f2f1;
    --hero-bg-light: #e9e7e8;
    --hero-bg-dark: #cfcdd0;
    --plum: #8a4a9c;
    --plum-deep: #5b2479;
    --plum-night: #3d1456;
    --lavender: #b79ad0;
    --lavender-soft: #e3d4f0;
    --blush: #b0569a;
    --arrow-pink: #d2457a;
    --gold: #d9b867;
    --cta-aqua: #45e3ef;
    --body-text: #4a4a4a;
    --white: #ffffff;
    --video-dark: #2b2420;
  }
  * { box-sizing: border-box; margin: 0; padding: 0; }
  html, body { width: 1200px; height: 675px; overflow: hidden; }
  body { background: var(--page-bg); font-family: "Lato", Arial, sans-serif; position: relative; }

  /* ---------- hero slider ---------- */
  .hero {
    position: absolute; left: 0; top: 0; width: 1200px; height: 176px;
    background: linear-gradient(90deg, var(--hero-bg-light), var(--hero-bg-dark) 40%, var(--hero-bg-light));
    overflow: hidden;
  }
  .hero-title-top {
    position: absolute; left: 247px; top: -42px;
    font-family: "Montserrat", sans-serif; font-weight: 800; font-size: 68px; letter-spacing: 3px; line-height: 1;
    color: transparent; -webkit-text-stroke: 2px var(--plum);
  }
  .hero-title-script {
    position: absolute; left: 284px; top: 4px;
    font-family: "Great Vibes", cursive; font-size: 84px; color: var(--plum); line-height: 1;
  }
  .hero-title-sub {
    position: absolute; left: 306px; top: 66px;
    font-family: "Great Vibes", cursive; font-size: 32px; color: var(--blush); line-height: 1;
  }
  .hero-cta {
    position: absolute; left: 247px; top: 117px; width: 240px; height: 26px;
    background: var(--plum); color: var(--white);
    font-family: "Lato", sans-serif; font-size: 10px; font-weight: 700; letter-spacing: 2.8px;
    display: flex; align-items: center; justify-content: center;
    box-shadow: 0 3px 0 #6e3a80;
  }
  .hero-photo {
    position: absolute; left: 604px; top: 0; width: 257px; height: 176px;
    background: linear-gradient(180deg, #f3f1ee 0%, #e9e4df 50%, #c9a85c 70%, #b8903f 100%);
  }
  .hero-arrow { position: absolute; top: 110px; }
  .hero-arrow.prev { left: 12px; }
  .hero-arrow.next { left: 1162px; }
  .hero-dots { position: absolute; top: 164px; left: 582px; display: flex; gap: 5px; z-index: 2; }
  .hero-dots span { width: 9px; height: 9px; border-radius: 50%; border: 1px solid #8b7fa0; background: var(--white); }
  .hero-dots span.active { background: #e9e4f0; }

  .zigzag { position: absolute; left: 0; top: 179px; width: 1200px; height: 16px; }

  /* ---------- upgraded opt-in card ---------- */
  .gift-card {
    position: absolute; left: 264px; top: 251px; width: 323px; height: 200px;
    background:
      radial-gradient(circle at 18% 12%, rgba(255,255,255,0.18), rgba(255,255,255,0) 45%),
      linear-gradient(125deg, #5a4fd6 0%, #7a3fbf 48%, var(--plum-deep) 100%);
    color: var(--white); overflow: hidden;
    box-shadow: 0 8px 18px rgba(61,20,86,0.28);
  }
  .gift-card::before {
    content: ""; position: absolute; inset: 7px;
    border: 1px solid rgba(217,184,103,0.7);
    pointer-events: none;
  }
  .gift-ribbon {
    position: absolute; left: 0; top: 0; width: 6px; height: 100%;
    background: var(--gold);
  }
  .gift-kicker {
    position: absolute; left: 22px; top: 16px;
    font-family: "Montserrat", sans-serif; font-weight: 600; font-size: 11px;
    letter-spacing: 3px; color: var(--gold);
  }
  .gift-head {
    position: absolute; left: 20px; top: 26px; line-height: 1;
    font-family: "Montserrat", sans-serif; white-space: nowrap;
  }
  .gift-head .gift-big { font-size: 46px; font-weight: 800; letter-spacing: 1px; }
  .gift-for {
    position: absolute; left: 22px; top: 74px;
    font-family: "Great Vibes", cursive; font-size: 26px; line-height: 1; color: var(--lavender-soft);
  }
  .gift-lines {
    position: absolute; left: 22px; top: 106px; font-size: 12px; line-height: 15px; color: var(--lavender-soft);
  }
  .gift-lines strong { font-weight: 900; font-size: 14px; color: var(--white); }
  .gift-cta {
    position: absolute; left: 22px; top: 166px; height: 24px; padding: 0 16px;
    background: var(--cta-aqua); color: var(--plum-night); border-radius: 12px;
    font-family: "Montserrat", sans-serif; font-weight: 800; font-size: 12px; letter-spacing: 1px;
    display: flex; align-items: center; gap: 6px;
    box-shadow: 0 3px 0 #1fa9b6;
  }
  .gift-book {
    position: absolute; left: 196px; top: 22px; width: 108px; height: 150px;
    background: linear-gradient(135deg, #f7f5f8, #d7dcea);
    box-shadow: -3px 0 0 #b9bfd2 inset, 6px 8px 14px rgba(20,0,40,0.45);
    transform: rotate(4deg);
  }

  /* ---------- video ---------- */
  .video-card {
    position: absolute; left: 605px; top: 253px; width: 319px; height: 196px;
    background: radial-gradient(ellipse at 60% 55%, #7a6a5a 0%, #4a3d33 50%, var(--video-dark) 100%);
    border: 2px solid #1e1a18; overflow: hidden;
  }
  .video-title {
    position: absolute; left: 0; top: 0; width: 100%; height: 42px;
    background: linear-gradient(180deg, rgba(0,0,0,0.6), rgba(0,0,0,0));
    color: var(--white); font-family: "Lato", sans-serif; font-size: 12px; padding: 11px 0 0 38px;
  }
  .channel-dot { position: absolute; left: 7px; top: 6px; width: 24px; height: 24px; border-radius: 50%; background: #3d5a8a; border: 1px solid #d9c27a; }
  .video-tools { position: absolute; right: 12px; top: 6px; display: flex; gap: 14px; color: var(--white); font-size: 10px; text-align: center; }
  .video-tools svg { display: block; margin: 0 auto 2px; }
  .play { position: absolute; left: 141px; top: 84px; }

  /* ---------- intro copy ---------- */
  .section-heading {
    position: absolute; left: 266px; top: 481px; white-space: nowrap;
    font-family: "Caveat", cursive; font-weight: 700; font-size: 22px; color: var(--plum);
  }
  .intro {
    position: absolute; left: 265px; top: 525px;
    font-size: 14px; line-height: 17px; color: var(--body-text); white-space: nowrap;
  }
  .intro p + p { margin-top: 11px; }

  .to-top { position: absolute; left: 1162px; top: 622px; }
</style>
</head>
<body>
  <section class="hero">
    <div class="hero-title-top">WEDDING</div>
    <div class="hero-title-script">Cake</div>
    <div class="hero-title-sub">of your dreams</div>
    <div class="hero-photo" role="img" aria-label="Photo of a white tiered wedding cake with pink roses on a gold glitter base"></div>
    <svg class="hero-arrow prev" width="16" height="20" viewBox="0 0 16 20"><path d="M12 2 L4 10 L12 18" fill="none" stroke="var(--arrow-pink)" stroke-width="3"/></svg>
    <svg class="hero-arrow next" width="16" height="20" viewBox="0 0 16 20"><path d="M4 2 L12 10 L4 18" fill="none" stroke="var(--arrow-pink)" stroke-width="3"/></svg>
    <div class="hero-cta">BROWSE WEDDING CAKES ›</div>
  </section>
  <div class="hero-dots"><span></span><span class="active"></span></div>

  <svg class="zigzag" viewBox="0 0 1200 16" preserveAspectRatio="none">
    <defs>
      <pattern id="teeth" width="10" height="16" patternUnits="userSpaceOnUse">
        <path d="M0 6 L5 14 L10 6 Z" fill="#ab8cc8"/>
      </pattern>
    </defs>
    <rect x="0" y="0" width="1200" height="2" fill="#d7a9c8"/>
    <rect x="0" y="2" width="1200" height="5" fill="#ab8cc8"/>
    <rect x="0" y="0" width="1200" height="16" fill="url(#teeth)"/>
  </svg>

  <aside class="gift-card">
    <div class="gift-ribbon"></div>
    <div class="gift-kicker">A</div>
    <div class="gift-head"><span class="gift-big">GIFT</span></div>
    <div class="gift-for">For You!</div>
    <div class="gift-lines">
      The Ultimate <strong>Bride's Guide</strong><br>For Buying <strong>A Wedding Cake</strong>
    </div>
    <div class="gift-cta">Get It Now !
      <svg width="10" height="10" viewBox="0 0 10 10"><path d="M2 1 L7 5 L2 9" fill="none" stroke="currentColor" stroke-width="2"/></svg>
    </div>
    <div class="gift-book" role="img" aria-label="Cover of the free bride's guide book to buying a wedding cake"></div>
  </aside>

  <div class="video-card" role="img" aria-label="Video still of the head baker presenting the cake showroom">
    <div class="video-title">The Sugar Atelier - Plorvex, NE</div>
    <div class="channel-dot"></div>
    <div class="video-tools">
      <div><svg width="14" height="14" viewBox="0 0 14 14"><circle cx="7" cy="7" r="6" fill="#fff"/><path d="M7 3.5 V7 L9.5 8.5" stroke="#222" stroke-width="1.4" fill="none"/></svg>Watch later</div>
      <div><svg width="14" height="14" viewBox="0 0 14 14"><path d="M8 2 L13 7 L8 12 V9 C4 9 2 10 1 12 C1.5 8 4 5.5 8 5 Z" fill="#fff"/></svg>Share</div>
    </div>
    <svg class="play" width="34" height="24" viewBox="0 0 34 24"><rect width="34" height="24" rx="6" fill="#212121" fill-opacity="0.85"/><path d="M13 7 L22 12 L13 17 Z" fill="#fff"/></svg>
  </div>

  <h2 class="section-heading">Feel confident about choosing the sugar atelier as your wedding cake baker/designer</h2>

  <div class="intro">
    <p>Each of the 22 dedicated and committed cakes artists and bakery staff consider it a privilege to offer you a FREE cake<br>testing and consultation that is the one of the best wedding cake experiences on the planet.</p>
    <p>While that sounds like bold claim that's hard to live up to, we don't settle for</p>
  </div>

  <svg class="to-top" width="20" height="20" viewBox="0 0 20 20"><circle cx="10" cy="10" r="10" fill="#3a3a3a"/><path d="M6 12 L10 8 L14 12" fill="none" stroke="#fff" stroke-width="1.8"/></svg>
</body>
</html>
```